WE ARE REACHING OUT TO CONTRACTORS TO HAVE AN OPPORTUNITY TO PROVIDE PROPOSALS FOR THEIR PROJECTS.

WE ARE A WASHINGTON DC. METRO AREA PLUMBING, HEATING AND AIR CONDITIONING CONTRACTOR. WE WOULD LIKE TO PRESENT A POSTCARD THAT OFFERS A FRENDLY, CONVENIENT WAY TO PROVIDE PROPOSALS FOR THEIR UP COMMING PROJECTS. WE WOULD APPRECIATE THE OPPURTUNITY TO PROVIDE ESTIMATES FOR YOUR UP COMMING PROJECTS. IF REQUESTED, WE WILL PROVIDE SAME DAY WALK THRU'S AND PROPOSALS. GET A 2ND OPINION, WE ALL LOOK AT PROJECTS DIFFERENTLY. CUSTOM HOMES, SUB DIVISIONS, REMODELING, SEWER AND WATER INSTALLATIONS AND REPLACEMENTS, WELL AND SEPTIC INSTALLATIONS AND REPAIRS, MECHANICAL EQUIPTMENT CHANGE OUTS, PLUMBING SYSTEMS REPLACEMENTS AND REPAIRS. RESIDENTAL AND COMERICAL CONSTRUCTION.. " WE DO IT ALL" JUST GIVE US A CALL. " WE WILL BE THERE " I WOULD LIKE MY BUSINESS CARD ON THE FRONT WITH SOME MODIFICATIONS AND THE ABOVE DESCRIPTION ON THE BACK. " HIGHLIGHTING WE WOULD APPRICATE THE OPPORTUNITY TO WORK WITH YOU COMPANY " SAME DAY WALK THRU'S AND PROPOSALS. PLEASE ADDRESS THE TOP OF THE BACK IN BOLD PRINT. " ATTENTION ESTIMATING " EYE CATCHING COLORS PLEASE. THANK YOU, TOM SELWYN

```html
<!DOCTYPE html>
<html lang="en">
<head>
<meta charset="utf-8">
<title>T.Selwyn Mechanical Services – Postcard</title>
<link href="https://fonts.googleapis.com/css2?family=Archivo+Black&family=Michroma&family=Roboto:wght@400;700&display=swap" rel="stylesheet">
<style>
  :root {
    --red: #e8232b;
    --white: #ffffff;
    --ink: #222222;
    --paper: #f2f2f2;
    --muted: #9a9a9a;
    --bg-top: #a9c9de;
    --bg-bottom: #e4eef5;
  }
  * { box-sizing: border-box; margin: 0; padding: 0; }
  html, body { width: 1200px; height: 1000px; overflow: hidden; }
  body {
    background: linear-gradient(180deg, var(--bg-top), var(--bg-bottom));
    font-family: "Roboto", Arial, sans-serif;
    position: relative;
  }
  .card {
    position: absolute;
    width: 560px;
    height: 370px;
    overflow: hidden;
    box-shadow: 0 12px 30px rgba(0,0,0,.22);
  }
  .card--front { left: 25px; top: 315px; background: var(--red); }
  .card--back  { left: 615px; top: 315px; background: var(--paper); }

  /* ---------- front ---------- */
  .front__top {
    position: absolute; left: 0; top: 0; width: 100%; height: 110px;
    background: var(--white);
  }
  .brand {
    position: absolute; top: 26px; left: 0; width: 100%;
    text-align: center;
  }
  .brand__name {
    display: inline-flex; align-items: center; gap: 10px;
    font-family: "Michroma", sans-serif; font-size: 30px; color: var(--red);
    line-height: 1;
  }
  .brand__mark { width: 22px; height: 22px; background: var(--red); }
  .brand__tagline {
    font-family: "Michroma", sans-serif; font-size: 11px; color: var(--ink);
    letter-spacing: 1px; margin-top: 8px;
  }
  .name-tab {
    position: absolute; left: 0; top: 128px; width: 215px; height: 40px;
    background: var(--white);
    box-shadow: 0 6px 10px rgba(0,0,0,.2);
    font-family: "Michroma", sans-serif; font-size: 17px; color: var(--red);
    line-height: 40px; padding-left: 24px;
  }
  .contact {
    position: absolute; left: 24px; top: 196px; color: var(--white);
    font-family: "Michroma", sans-serif;
  }
  .contact__phone { font-size: 19px; }
  .contact__email { font-size: 10px; margin-top: 6px; }
  .contact__address { font-size: 10px; line-height: 1.6; margin-top: 22px; }
  .divider {
    position: absolute; left: 252px; top: 186px; width: 1px; height: 160px;
    background: rgba(255,255,255,.7);
  }
  .experience {
    position: absolute; left: 270px; top: 186px; color: var(--white);
    font-family: "Michroma", sans-serif;
  }
  .experience__years { font-size: 24px; font-weight: 400; }
  .experience__scope { font-size: 8.5px; line-height: 1.5; margin-top: 2px; }
  .services {
    list-style: none; position: absolute; left: 270px; top: 252px;
    font-family: "Michroma", sans-serif; font-size: 12.5px; color: var(--white);
    line-height: 23px;
  }
  .stripes { position: absolute; }
  .stripes--front { right: 0; bottom: 16px; }

  /* ---------- back ---------- */
  .back__header {
    position: absolute; left: 0; top: 0; width: 100%; height: 150px;
    background: var(--red);
  }
  .headline {
    position: absolute; top: 34px; left: 0; width: 100%; text-align: center;
    font-family: "Archivo Black", sans-serif; line-height: 1;
  }
  .headline__top { font-size: 38px; color: var(--white); letter-spacing: 1px; }
  .headline__bottom { font-size: 42px; color: var(--ink); letter-spacing: 1px; margin-top: 2px; }
  .stripes--left { left: 0; top: 26px; }
  .stripes--right { right: 0; top: 86px; }
  .pitch {
    position: absolute; left: 22px; top: 166px; width: 290px;
    font-size: 10.5px; line-height: 1.45; color: var(--ink);
  }
  .pitch__lead { color: var(--red); font-weight: 700; margin-bottom: 8px; }
  .pitch p + p { margin-top: 8px; }
  .slogan {
    position: absolute; left: 322px; top: 166px; width: 230px; text-align: center;
    font-family: "Archivo Black", sans-serif; font-size: 15px; line-height: 1.3;
  }
  .slogan__accent { color: var(--red); }
  .slogan__plain { color: var(--ink); font-family: "Roboto", sans-serif; font-weight: 400; font-size: 15px; }
  .address-box {
    position: absolute; left: 345px; top: 244px; width: 190px; height: 108px;
    background: var(--white); border: 1px solid #d6d6d6;
    box-shadow: 3px 4px 0 #c9c9c9;
    display: flex; align-items: center; justify-content: center;
    font-size: 15px; color: var(--muted);
  }
</style>
</head>
<body>

<section class="card card--front" aria-label="Postcard front">
  <div class="front__top">
    <div class="brand">
      <div class="brand__name"><span class="brand__mark"></span>T.SELWYN</div>
      <div class="brand__tagline">MECHANICAL SERVICES</div>
    </div>
  </div>

  <div class="name-tab">TOM SELWYN</div>

  <div class="contact">
    <div class="contact__phone">301-555-0142</div>
    <div class="contact__email">TOMSELWYN@MAILBOX.COM</div>
    <div class="contact__address">1180 ALDER MILL ROAD<br>LINDEN PARK, MD 21000</div>
  </div>

  <div class="divider"></div>

  <div class="experience">
    <div class="experience__years">36 YEARS</div>
    <div class="experience__scope">RESIDENTIAL AND COMMERCIAL<br>CONSTRUCTION AND REMODELING</div>
  </div>

  <ul class="services">
    <li>HEATING</li>
    <li>PLUMBING</li>
    <li>GAS FITTING</li>
    <li>AIR CONDITIONING</li>
  </ul>

  <svg class="stripes stripes--front" width="96" height="64" viewBox="0 0 96 64">
    <polygon points="16,0 96,0 96,14 0,14" fill="#ffffff"/>
    <polygon points="16,25 96,25 96,39 16,39 0,32" fill="#ffffff"/>
    <polygon points="0,50 96,50 96,64 16,64" fill="#ffffff"/>
  </svg>
</section>

<section class="card card--back" aria-label="Postcard back">
  <div class="back__header">
    <svg class="stripes stripes--left" width="70" height="56" viewBox="0 0 70 56">
      <polygon points="0,0 55,0 70,8 55,16 0,16" fill="#ffffff"/>
      <polygon points="0,20 55,20 70,28 55,36 0,36" fill="#ffffff"/>
      <polygon points="0,40 55,40 70,48 55,56 0,56" fill="#ffffff"/>
    </svg>
    <div class="headline">
      <div class="headline__top">ATTENTION</div>
      <div class="headline__bottom">ESTIMATING</div>
    </div>
    <svg class="stripes stripes--right" width="70" height="56" viewBox="0 0 70 56">
      <polygon points="15,0 70,0 70,16 15,16 0,8" fill="#ffffff"/>
      <polygon points="15,20 70,20 70,36 15,36 0,28" fill="#ffffff"/>
      <polygon points="15,40 70,40 70,56 15,56 0,48" fill="#ffffff"/>
    </svg>
  </div>

  <div class="pitch">
    <p class="pitch__lead">We would appreciate the opportunity to work with your company on your upcoming projects. We provide same day walk thru's and proposals.</p>
    <p>Get a 2nd opinion, we all look at projects differently.</p>
    <p>Custom homes, sub divisions, remodeling, sewer and water installations and replacements, well and septic installations and repairs, mechanical equipment change outs, plumbing systems replacements and repairs. Residential and commercial construction.</p>
  </div>

  <div class="slogan">
    <div class="slogan__accent">“WE DO IT ALL”</div>
    <div class="slogan__plain">JUST GIVE US A CALL.</div>
    <div class="slogan__accent">“WE WILL BE THERE”</div>
  </div>

  <div class="address-box">Address Here</div>
</section>

</body>
</html>
```